Stationary for Tovin Consulting

Hi

I am after stationary designs for my company - Tovin Consulting. I have a logo - recently designed by ArtHarbor. Tovin ( nivot spelt backwards ) is a sales consultancy - including sales training, sales coaching and business management.

I have attached some of the artwork I already have, as well as a few ideas
1. Use supplied logo's
2. back of business card to use the logo with the dark background and white text
3. details to be included on card are
Logo
Delia Marquand
p: +61409827316
e: delia@tovinconsulting.com.au
w: www.tovinconsulting.com.au
PO Box 412, Kelby Heights, Victoria, 3187

4. I am after designs for business cards, A4 letterhead and A5 letterhead

Thanks in Advance

Delia

Industry/Entity Type

It Company

```html
<!DOCTYPE html>
<html lang="en">
<head>
<meta charset="utf-8">
<title>Tovin Consulting – Business Card</title>
<link rel="stylesheet" href="https://fonts.googleapis.com/css2?family=Open+Sans:wght@400;600;700&family=Ubuntu:wght@700&display=swap">
<style>
  :root {
    --slate: #2f4551;
    --slate-light: #5d6b74;
    --accent: #e2411d;
    --paper: #ffffff;
    --rule: #8a9298;
    --muted: #7b848a;
    --backdrop: #d9d9d6;
  }
  html, body {
    margin: 0;
    width: 1200px;
    height: 900px;
    overflow: hidden;
    background: var(--backdrop);
    font-family: "Open Sans", sans-serif;
  }
  .canvas {
    position: relative;
    width: 1200px;
    height: 900px;
  }
  .card {
    position: absolute;
    left: 270px;
    width: 660px;
    height: 377px;
    border-radius: 28px;
    overflow: hidden;
    box-shadow: 0 6px 18px rgba(0,0,0,.18);
  }
  .card--front { top: 50px; background: var(--paper); }
  .card--back { top: 470px; background: var(--slate); }

  .wordmark {
    position: absolute;
    font-family: "Ubuntu", sans-serif;
    font-weight: 700;
    letter-spacing: -0.5px;
    display: flex;
    align-items: center;
    gap: 12px;
    margin: 0;
  }
  .wordmark__square { width: 22px; height: 22px; }
  .card--front .wordmark { left: 40px; top: 58px; font-size: 42px; color: var(--slate); }
  .card--front .wordmark__square { background: var(--accent); }
  .card--back .wordmark { right: 60px; top: 150px; font-size: 44px; color: var(--paper); }
  .card--back .wordmark__square { background: var(--paper); }

  .holder {
    position: absolute;
    right: 36px;
    top: 98px;
    text-align: right;
  }
  .holder__name {
    font-weight: 700;
    font-size: 20px;
    letter-spacing: 1px;
    color: var(--slate);
    margin: 0;
  }
  .holder__title {
    font-size: 12px;
    color: var(--muted);
    letter-spacing: 1px;
    margin: 6px 0 0;
  }
  .divider {
    position: absolute;
    left: 40px;
    right: 36px;
    top: 131px;
    height: 1px;
    background: var(--rule);
  }
  .contacts {
    position: absolute;
    left: 40px;
    top: 196px;
    margin: 0;
    padding: 0;
    list-style: none;
    font-size: 17px;
    color: var(--slate);
    letter-spacing: 0.5px;
  }
  .contacts li {
    display: flex;
    align-items: center;
    gap: 12px;
    height: 26px;
  }
  .contacts svg { width: 16px; height: 16px; flex: none; }

  .bands {
    position: absolute;
    left: 0;
    bottom: 0;
    width: 660px;
    height: 110px;
  }
  .address {
    position: absolute;
    left: 40px;
    bottom: 9px;
    margin: 0;
    font-size: 15px;
    font-weight: 700;
    color: var(--paper);
    letter-spacing: 0.3px;
    white-space: nowrap;
  }
  .tagline {
    position: absolute;
    right: 30px;
    bottom: 42px;
    margin: 0;
    font-size: 14px;
    font-weight: 600;
    color: var(--paper);
    letter-spacing: 0.5px;
    white-space: nowrap;
  }
</style>
</head>
<body>
<main class="canvas">

  <section class="card card--front" aria-label="Business card front">
    <h1 class="wordmark"><span class="wordmark__square"></span>Tovin Consulting</h1>

    <div class="holder">
      <p class="holder__name">DELIA MARQUAND</p>
      <p class="holder__title">President</p>
    </div>
    <div class="divider"></div>

    <ul class="contacts">
      <li>
        <svg viewBox="0 0 16 16" aria-hidden="true"><path fill="#e2411d" d="M3 2h3l1.5 3.5-2 1.2a8 8 0 0 0 3.8 3.8l1.2-2L14 10v3a1 1 0 0 1-1 1A12 12 0 0 1 2 3a1 1 0 0 1 1-1z"/></svg>
        +61409827316
      </li>
      <li>
        <svg viewBox="0 0 16 16" aria-hidden="true"><rect x="1.5" y="3.5" width="13" height="9" fill="none" stroke="#e2411d" stroke-width="1.5"/><path d="M1.5 3.5 8 9l6.5-5.5" fill="none" stroke="#e2411d" stroke-width="1.5"/></svg>
        delia@tovinconsulting.com.au
      </li>
      <li>
        <svg viewBox="0 0 16 16" aria-hidden="true"><g fill="none" stroke="#e2411d" stroke-width="1.3"><circle cx="8" cy="8" r="6.5"/><ellipse cx="8" cy="8" rx="3" ry="6.5"/><path d="M1.5 8h13M2.5 4.8h11M2.5 11.2h11"/></g></svg>
        www.tovinconsulting.com.au
      </li>
    </ul>

    <svg class="bands" viewBox="0 0 660 110" preserveAspectRatio="none" aria-hidden="true">
      <defs>
        <linearGradient id="band-slate" x1="0" y1="0" x2="0" y2="1">
          <stop offset="0" stop-color="#5d6b74"/>
          <stop offset="1" stop-color="#2f4551"/>
        </linearGradient>
      </defs>
      <path fill="#e2411d" d="M0 72H362C380 72 380 22 402 20H660V110H0Z"/>
      <path fill="url(#band-slate)" d="M378 110C396 110 392 30 418 30H660V110Z"/>
    </svg>
    <p class="address">PO Box 412, Kelby Heights, Victoria, 3187</p>
    <p class="tagline">Your Business is Our Business</p>
  </section>

  <section class="card card--back" aria-label="Business card back">
    <h2 class="wordmark"><span class="wordmark__square"></span>Tovin Consulting</h2>
  </section>

</main>
</body>
</html>
```